Used Semi Truck Website Redesign

We are redoing the website backend and would like to also do a front end redesign. I would like a Mobile and Desktop mockup for each page. The website has more mobile visitors than desktop visitors. Our competitor is http://www.haulmarketbay.example. We don't want to copy them exactly but we want a site that looks more like that. We need the functionality of that site. One big difference is that we also sell parts and trailers.

We need a redesign for front page, product detail page, search result page, content page. It is very important that the site is very easy to use on mobile devices. Our target audience is Truck drivers.

Feel free to use demo fonts stock images, and icons. We will purchase necessary 3rd party media when a winner is chosen.

Target Market(s)

People who want to buy used trucks.

Coding

Coded - Design and coding required

Number of Pages Required

5+ page

Requirements
Must have
• Mockup for Desktop and Mobile pages.

```html
<!DOCTYPE html>
<html lang="en">
<head>
<meta charset="utf-8">
<title>Truck drivers – sell parts and trailers</title>
<link rel="stylesheet" href="https://fonts.googleapis.com/css2?family=Oswald:wght@400;500&family=Roboto:wght@400;500&display=swap">
<style>
:root{
  --orange:#ff6a00;
  --ink:#222;
  --muted:#666;
  --line:#e5e5e5;
  --dark:#0f151b;
  --topbar:#0c1116;
  --red:#ef5858;
  --green:#8da832;
  --cyan:#20c4e4;
  --blue:#2b5596;
}
*{box-sizing:border-box;margin:0;padding:0}
html,body{width:1200px;height:2419px;overflow:hidden}
body{position:relative;background:#fff;font-family:"Roboto",Arial,sans-serif;color:var(--ink);font-size:12px}
a{color:inherit;text-decoration:none}
ul{list-style:none}
.abs{position:absolute}

/* top bar */
.topbar{left:0;top:0;width:1200px;height:32px;background:var(--topbar);color:#fff;font-size:12px}
.topbar .count{left:90px;top:9px}
.topbar .links{right:88px;top:9px}
.topbar .links span{margin:0 4px;color:#aaa}

/* hero */
.hero{left:0;top:32px;width:1200px;height:384px;
  background:linear-gradient(100deg,#3a3c3f 0%,#6d6f72 35%,#8a8c8e 55%,#4a5466 75%,#1f2a44 100%)}
.logo{left:90px;top:52px;color:#fff}
.logo .name{font-family:"Roboto",sans-serif;font-size:24px;line-height:1.1;font-weight:500;color:#fff}
.logo .tag{font-size:11px;margin-top:1px}
.nav{left:553px;top:64px;color:#fff;font-size:13px;display:flex;align-items:center}
.nav a{padding:0 14px;border-right:1px solid rgba(255,255,255,.35)}
.nav a:last-child{border:0}
.social{left:740px;top:58px;display:flex;gap:8px}
.social i{display:block;width:26px;height:26px;border-radius:50%;background:#1a1d22}
.promo{left:884px;top:40px;width:226px;height:57px;background:rgba(40,44,52,.85);text-align:center;padding-top:6px}
.promo .cta{font-family:"Oswald",sans-serif;font-size:24px;line-height:1;color:var(--orange)}
.promo .url{font-family:"Oswald",sans-serif;font-size:13px;color:#fff}
.welcome{left:0;top:182px;width:1200px;text-align:center;color:#fff}
.welcome h1{font-family:"Oswald",sans-serif;font-weight:400;font-size:33px;line-height:1.1}
.welcome p{font-size:14px}

/* quick search */
.search{left:235px;top:256px;width:730px;height:204px;background:#fff;box-shadow:0 2px 8px rgba(0,0,0,.12)}
.search-head{height:42px;background:var(--orange);color:#fff;font-size:17px;display:flex;align-items:center;padding-left:34px;gap:10px}
.fields{padding:21px 31px 0;display:grid;grid-template-columns:221px 221px 221px;gap:9px 7px}
.field{height:36px;border:1px solid #ddd;font-size:11px;color:#444;display:flex;align-items:center;justify-content:space-between;padding:0 14px}
.field .caret{width:0;height:0;border:4px solid transparent;border-top-color:#666;border-bottom:0}
.search-foot{position:absolute;left:0;bottom:0;width:730px;height:42px;background:#f4f4f4;display:flex;align-items:center}
.search-foot .adv{padding-left:30px;font-size:13px;color:#333;display:flex;align-items:center;gap:10px}
.search-foot .adv::before{content:"";border:5px solid transparent;border-left:7px solid var(--orange);border-right:0}
.search-foot .go{margin-left:auto;width:220px;height:42px;background:var(--topbar);color:#fff;font-size:13px;font-weight:500;display:flex;align-items:center;justify-content:center;letter-spacing:.3px}

/* category cards */
.cat{left:89px;width:721px;height:279px;border:1px solid var(--line)}
.cat h2{position:absolute;left:30px;top:17px;font-size:19px;font-weight:400;color:#111}
.cat .sub{position:absolute;left:30px;top:42px;font-size:12px;color:#444}
.cat .rule{position:absolute;left:18px;right:16px;top:66px;border-top:1px solid var(--line)}
.cat .icons{position:absolute;left:32px;top:120px;display:flex;gap:27px}
.cat .ic{width:72px;text-align:center;font-size:11px;line-height:1.3;color:#222}
.cat .ic .disc{width:72px;height:72px;border-radius:50%;display:flex;align-items:center;justify-content:center;margin-bottom:6px}
.cat .ic svg{width:40px;height:40px}
.cat .types{position:absolute;left:432px;top:86px;font-size:12px;line-height:20.5px;color:#333}
.cat .more{color:var(--orange)}
.red .disc{background:var(--red)}
.green .disc{background:var(--green)}
.cyan .disc{background:var(--cyan)}
.blue .disc{background:var(--blue)}

/* sidebar */
.side{left:836px;width:274px}
.side-row{height:34px;border-bottom:1px solid var(--line);display:flex;align-items:center;justify-content:space-between;padding:0 16px 0 24px;font-size:15px;color:#222}
.chev{width:7px;height:7px;border-top:2px solid #222;border-right:2px solid #222;transform:rotate(45deg)}
.side-row.open{color:var(--orange);border:0}
.side-row.open .chev{border-color:var(--orange);transform:rotate(135deg)}
.makes{padding:8px 0 10px 37px;font-size:12px;line-height:24px;color:#333;border-bottom:1px solid var(--line)}
.makes li{display:flex;align-items:center;gap:11px}
.makes li::before{content:"";width:5px;height:5px;border-radius:50%;background:#555}
.ad{left:836px;top:1027px;width:274px;height:313px;background:linear-gradient(180deg,#7e8380 0%,#5d6361 55%,#9ea4a6 100%)}
.ad-frame{left:849px;top:1042px;width:248px;height:226px;border:1px solid rgba(255,255,255,.25)}
.ad-label{left:836px;top:1150px;width:274px;text-align:center;color:#fff;font-family:"Oswald",sans-serif;font-size:24px;line-height:1.15}
.blog{left:836px;top:1352px;width:274px;height:314px;border:1px solid var(--line);padding:24px 20px 0 28px}
.blog h3{font-size:15px;font-weight:400;margin-bottom:10px}
.blog li{position:relative;padding:10px 0 12px 15px;border-bottom:1px solid var(--line);font-size:11px;line-height:17px;color:#444}
.blog li:last-child{border:0}
.blog li::before{content:"›";position:absolute;left:2px;top:9px;color:#888}
.blog time{display:block;color:#222;font-size:11px;margin-top:2px}

/* featured */
.featured-title{left:0;top:1713px;width:1200px;text-align:center;font-size:27px;color:#222}
.featured-all{right:90px;top:1723px;font-size:12px;color:var(--orange)}
.listing{top:1763px;width:245px}
.listing .photo{height:185px}
.listing h4{font-size:14px;font-weight:400;margin-top:17px;color:#222}
.listing .price{font-size:13px;color:#777;margin-top:3px}

/* dealer band */
.dealer{left:0;top:2058px;width:1200px;height:87px;background:var(--orange);color:#fff}
.dealer svg{position:absolute;left:86px;top:22px}
.dealer h3{position:absolute;left:130px;top:25px;font-weight:400;font-size:21px}
.dealer p{position:absolute;left:131px;top:51px;font-size:13px}
.dealer .btn{position:absolute;left:960px;top:26px;width:150px;height:39px;background:#111;color:#fff;font-size:12px;display:flex;align-items:center;justify-content:center}

/* footer */
.footer{left:0;top:2145px;width:1200px;height:274px;background:var(--dark);color:#fff}
.fcol{top:44px}
.fcol h5{font-size:15px;font-weight:400;margin-bottom:14px}
.fcol li{font-size:12px;line-height:28.5px;display:flex;align-items:center;gap:10px}
.arrow{width:10px;height:8px}
.follow li{line-height:34px;gap:12px}
.follow .dot{width:25px;height:25px;border-radius:50%}
.feed li{align-items:flex-start;line-height:17px;margin-bottom:30px}
.feed .dot{flex:none;width:14px;height:14px;border-radius:50%;background:#2aa9e0;margin-top:2px}
.fbottom{left:87px;top:2374px;width:1023px;border-top:1px solid #232b33}
.copy{left:87px;top:2390px;font-size:12px}
.legal{right:90px;top:2390px;font-size:12px}
.totop{left:1132px;top:2346px;width:34px;height:34px;border-radius:50%;background:var(--orange);display:flex;align-items:center;justify-content:center}
</style>
</head>
<body>

<svg width="0" height="0" style="position:absolute" aria-hidden="true">
  <defs>
    <symbol id="i-sleeper" viewBox="0 0 40 40"><rect x="3" y="13" width="20" height="13" rx="1" fill="#fff"/><path d="M24 17h7l5 5v4H24z" fill="#fff"/><circle cx="10" cy="29" r="3" fill="#fff"/><circle cx="30" cy="29" r="3" fill="#fff"/></symbol>
    <symbol id="i-dump" viewBox="0 0 40 40"><path d="M4 12h22l-3 11H6z" fill="#fff"/><path d="M27 16h6l4 5v5H27z" fill="#fff"/><rect x="4" y="23" width="23" height="3" fill="#fff"/><circle cx="11" cy="29" r="3" fill="#fff"/><circle cx="31" cy="29" r="3" fill="#fff"/></symbol>
    <symbol id="i-daycab" viewBox="0 0 40 40"><rect x="10" y="6" width="20" height="22" rx="2" fill="#fff"/><rect x="13" y="9" width="14" height="7" fill="rgba(0,0,0,.25)"/><rect x="8" y="28" width="24" height="3" fill="#fff"/><rect x="11" y="31" width="4" height="4" fill="#fff"/><rect x="25" y="31" width="4" height="4" fill="#fff"/></symbol>
    <symbol id="i-tow" viewBox="0 0 40 40"><path d="M3 19h16l4-5h8l6 6v6H3z" fill="#fff"/><path d="M6 19l8-9" stroke="#fff" stroke-width="2"/><circle cx="10" cy="28" r="3" fill="#fff"/><circle cx="29" cy="28" r="3" fill="#fff"/></symbol>
    <symbol id="i-wrench" viewBox="0 0 40 40"><path d="M9 31l20-20M11 9l20 20" stroke="#fff" stroke-width="4" stroke-linecap="round"/><circle cx="29" cy="11" r="4" fill="none" stroke="#fff" stroke-width="2"/></symbol>
    <symbol id="i-spanner" viewBox="0 0 40 40"><path d="M15 6v28M25 6v28" stroke="#fff" stroke-width="4" stroke-linecap="round"/><circle cx="15" cy="20" r="3" fill="#fff"/><circle cx="25" cy="14" r="3" fill="#fff"/></symbol>
    <symbol id="i-gear" viewBox="0 0 40 40"><circle cx="20" cy="20" r="12" fill="none" stroke="#fff" stroke-width="4" stroke-dasharray="4 3"/><circle cx="20" cy="20" r="5" fill="#fff"/></symbol>
    <symbol id="i-piston" viewBox="0 0 40 40"><rect x="20" y="5" width="13" height="11" rx="2" fill="#fff" transform="rotate(45 26 10)"/><path d="M22 18L8 32" stroke="#fff" stroke-width="4" stroke-linecap="round"/></symbol>
  </defs>
</svg>

<!-- top bar -->
<div class="abs topbar">
  <span class="abs count">256,140 trucks and trailers for sale</span>
  <span class="abs links">MyHauler: Login <span>|</span> Register <span>|</span> Find a Dealer <span>|</span> Dealer Login</span>
</div>

<!-- hero -->
<div class="abs hero" role="img" aria-label="Photo of a blue semi truck on an open road under a grey sky"></div>
<div class="abs logo"><div class="name">Truck drivers</div><div class="tag">sell parts and trailers</div></div>
<nav class="abs nav"><a>Find</a><a>Sell</a><a>Research</a></nav>
<div class="abs social"><i></i><i></i><i></i><i></i></div>
<div class="abs promo"><div class="cta">CLICK HERE</div><div class="url">WWW.EXAMPLE.COM</div></div>
<div class="abs welcome"><h1>Welcome To Truck Drivers</h1><p>sell parts and trailers</p></div>

<section class="abs search">
  <div class="search-head">
    <svg width="16" height="16" viewBox="0 0 16 16"><circle cx="6.5" cy="6.5" r="5" fill="none" stroke="#fff" stroke-width="2"/><path d="M10.5 10.5l4 4" stroke="#fff" stroke-width="2"/></svg>
    Quick Search
  </div>
  <div class="fields">
    <div class="field">Keyword</div>
    <div class="field">Set a Class<span class="caret"></span></div>
    <div class="field">Select a Category<span class="caret"></span></div>
    <div class="field">Select a Make<span class="caret"></span></div>
    <div class="field">Zip Code</div>
    <div class="field">Any Distance<span class="caret"></span></div>
  </div>
  <div class="search-foot"><span class="adv">Advanced Search</span><a class="go">SEARCH NOW</a></div>
</section>

<!-- categories -->
<section class="abs cat red" style="top:510px">
  <h2>Find Heavy Duty Trucks For Sale</h2>
  <p class="sub">What Type Heavy Duty Truck do you need?</p>
  <div class="rule"></div>
  <div class="icons">
    <div class="ic"><div class="disc"><svg><use href="#i-sleeper"/></svg></div>Conventional Sleeper Truck</div>
    <div class="ic"><div class="disc"><svg><use href="#i-dump"/></svg></div>Dump-Truck</div>
    <div class="ic"><div class="disc"><svg><use href="#i-daycab"/></svg></div>Conventional Day Cab</div>
    <div class="ic"><div class="disc"><svg><use href="#i-tow"/></svg></div>Wrecker Tow Truck</div>
  </div>
  <ul class="types"><li>Cab-Chassis</li><li>Flatbed-Truck</li><li>Box Truck-Straight Truck</li><li>Day Cab</li><li>Tractor</li><li>Crane Truck</li><li>Bucket Truck - Boom Truck</li><li class="more">See All Heavy Duty Trucks →</li></ul>
</section>

<section class="abs cat green" style="top:805px">
  <h2>Find Medium Duty Trucks For Sale</h2>
  <p class="sub">What Type of Medium Duty Truck do you need?</p>
  <div class="rule"></div>
  <div class="icons">
    <div class="ic"><div class="disc"><svg><use href="#i-sleeper"/></svg></div>Conventional Sleeper Truck</div>
    <div class="ic"><div class="disc"><svg><use href="#i-dump"/></svg></div>Dump-Truck</div>
    <div class="ic"><div class="disc"><svg><use href="#i-daycab"/></svg></div>Conventional Day Cab</div>
    <div class="ic"><div class="disc"><svg><use href="#i-tow"/></svg></div>Wrecker Tow Truck</div>
  </div>
  <ul class="types"><li>Rollback Tow Truck</li><li>Utility Truck - Service Truck</li><li>Crew Cab</li><li>Refrigerated Truck</li><li>Wrecker Tow Truck</li><li>Bucket Truck - Boom Truck</li><li>Flatbed</li><li class="more">See All Heavy Duty Trucks →</li></ul>
</section>

<section class="abs cat cyan" style="top:1095px">
  <h2>Find Light Duty Trucks For Sale</h2>
  <p class="sub">What Type of Light Duty Truck do you need?</p>
  <div class="rule"></div>
  <div class="icons">
    <div class="ic"><div class="disc"><svg><use href="#i-wrench"/></svg></div>Conventional Sleeper Truck</div>
    <div class="ic"><div class="disc"><svg><use href="#i-spanner"/></svg></div>Dump-Truck</div>
    <div class="ic"><div class="disc"><svg><use href="#i-gear"/></svg></div>Conventional Day Cab</div>
    <div class="ic"><div class="disc"><svg><use href="#i-piston"/></svg></div>Wrecker Tow Truck</div>
  </div>
  <ul class="types"><li>Dump Truck</li><li>Crew Cab</li><li>Flatbed Truck</li><li>Van</li><li>Passenger Van</li><li>Cutaway-Cube Van</li><li>Refrigerated Truck</li><li class="more">See All Heavy Duty Trucks →</li></ul>
</section>

<section class="abs cat blue" style="top:1390px">
  <h2>Find Truck Trailers For Sale</h2>
  <p class="sub">What Type of Trailer do you need?</p>
  <div class="rule"></div>
  <div class="icons">
    <div class="ic"><div class="disc"><svg><use href="#i-sleeper"/></svg></div>Conventional Sleeper Truck</div>
    <div class="ic"><div class="disc"><svg><use href="#i-dump"/></svg></div>Dump-Truck</div>
    <div class="ic"><div class="disc"><svg><use href="#i-daycab"/></svg></div>Conventional Day Cab</div>
    <div class="ic"><div class="disc"><svg><use href="#i-tow"/></svg></div>Wrecker Tow Truck</div>
  </div>
  <ul class="types"><li>Dump Trailer</li><li>Lowboy Trailer</li><li>Reefer Van</li><li>Gooseneck Trailer</li><li>End Dump Trailer</li><li>Utility Trailer</li><li>Drop Deck</li><li class="more">See All Heavy Duty Trucks →</li></ul>
</section>

<!-- sidebar -->
<aside class="abs side" style="top:498px">
  <div class="side-row">Trucks for sale by State <span class="chev"></span></div>
  <div class="side-row open" style="margin-top:9px">Trucks for sale by Make <span class="chev"></span></div>
  <ul class="makes">
    <li>Ardent</li><li>Frontline</li><li>Cobalt</li><li>Petra Works</li><li>Interstate Motors</li><li>Kenridge</li><li>Ramsey</li><li>Gantry</li><li>Izumo</li><li>Marlow</li><li>Valdor</li><li>Dorsey</li><li>Hinata</li><li>Stratton</li><li>Meridian</li><li>Norland</li>
  </ul>
  <div class="side-row" style="margin-top:14px;border:0">Resource Advertisers <span class="chev"></span></div>
</aside>
<div class="abs ad" role="img" aria-label="Advertising photo of a white semi truck on a highway"></div>
<div class="abs ad-frame"></div>
<div class="abs ad-label">ADVERTISMENT<br>52X58</div>

<aside class="abs blog">
  <h3>Truck Blog</h3>
  <ul>
    <li>Donec quam felis ultricies nec pellente sque eu pretium quis sem .<time>9:26 AM November 24th</time></li>
    <li>Donec quam felis ultricies nec pellente sque eu pretium quis sem .<time>9:26 AM November 24th</time></li>
    <li>Donec quam felis ultricies nec pellente sque eu pretium quis sem .<time>9:26 AM November 24th</time></li>
  </ul>
</aside>

<!-- featured -->
<h2 class="abs featured-title" style="font-weight:400">Featured Ads</h2>
<a class="abs featured-all">View all featured trucks and trailers for sale →</a>
<article class="abs listing" style="left:89px"><div class="photo" role="img" aria-label="Photo of assorted truck engine parts and tools" style="background:linear-gradient(135deg,#cfd2d4,#8d9296 60%,#5b6064)"></div><h4>2016 Brantley ROADSTER</h4><p class="price">$37,500.00</p></article>
<article class="abs listing" style="left:347px"><div class="photo" role="img" aria-label="Photo of a black semi truck on a road" style="background:linear-gradient(160deg,#e9ecee,#9ea3a7 50%,#2b2e32)"></div><h4>2016 Brantley ROADSTER</h4><p class="price">$37,500.00</p></article>
<article class="abs listing" style="left:605px"><div class="photo" role="img" aria-label="Photo of a truck engine close up" style="background:linear-gradient(135deg,#b9bcbf,#6e7377 55%,#3a3e42)"></div><h4>2016 Brantley ROADSTER</h4><p class="price">$37,500.00</p></article>
<article class="abs listing" style="left:865px"><div class="photo" role="img" aria-label="Photo of an orange dump truck on a dirt site" style="background:linear-gradient(180deg,#c9ccd2,#9a8f84 45%,#d4702a 70%,#7a6a5a)"></div><h4>2016 Brantley ROADSTER</h4><p class="price">$37,500.00</p></article>

<!-- dealer band -->
<section class="abs dealer">
  <svg width="30" height="42" viewBox="0 0 30 42"><path d="M15 1C7.3 1 1 7.2 1 14.8 1 25 15 41 15 41s14-16 14-26.2C29 7.2 22.7 1 15 1z" fill="#fff"/><circle cx="15" cy="14.5" r="5.5" fill="var(--orange)"/></svg>
  <h3>Find a Dealer</h3>
  <p>Find Commercial Truck dealers by name, make and location.</p>
  <a class="btn">FIND A DEALER</a>
</section>

<!-- footer -->
<footer class="abs footer">
  <div class="abs fcol" style="left:87px">
    <h5>Explore Our Site</h5>
    <ul>
      <li><svg class="arrow" viewBox="0 0 10 8"><path d="M0 4h9M6 1l3 3-3 3" stroke="#fff" fill="none"/></svg>Trucks for Sale</li>
      <li><svg class="arrow" viewBox="0 0 10 8"><path d="M0 4h9M6 1l3 3-3 3" stroke="#fff" fill="none"/></svg>Truck Resources</li>
      <li><svg class="arrow" viewBox="0 0 10 8"><path d="M0 4h9M6 1l3 3-3 3" stroke="#fff" fill="none"/></svg>New Truck Models</li>
      <li><svg class="arrow" viewBox="0 0 10 8"><path d="M0 4h9M6 1l3 3-3 3" stroke="#fff" fill="none"/></svg>Check Truck Prices</li>
    </ul>
  </div>
  <div class="abs fcol" style="left:342px">
    <h5>Sell Truck &amp; Parts</h5>
    <ul>
      <li><svg class="arrow" viewBox="0 0 10 8"><path d="M0 4h9M6 1l3 3-3 3" stroke="#fff" fill="none"/></svg>Private Truck Sellers</li>
      <li><svg class="arrow" viewBox="0 0 10 8"><path d="M0 4h9M6 1l3 3-3 3" stroke="#fff" fill="none"/></svg>Truck Dealers</li>
      <li><svg class="arrow" viewBox="0 0 10 8"><path d="M0 4h9M6 1l3 3-3 3" stroke="#fff" fill="none"/></svg>Advertise on Commercial</li>
      <li><svg class="arrow" viewBox="0 0 10 8"><path d="M0 4h9M6 1l3 3-3 3" stroke="#fff" fill="none"/></svg>sell parts</li>
    </ul>
  </div>
  <div class="abs fcol follow" style="left:634px">
    <h5>Follow Us</h5>
    <ul>
      <li><span class="dot" style="background:var(--orange)"></span>Blog</li>
      <li><span class="dot" style="background:#3b5b98"></span>Facesheet</li>
      <li><span class="dot" style="background:#2aa9e0"></span>Chirper</li>
      <li><span class="dot" style="background:#e5403b"></span>Reelcast</li>
    </ul>
  </div>
  <div class="abs fcol feed" style="left:855px;width:250px">
    <h5>Chirper Feed</h5>
    <ul>
      <li><span class="dot"></span>@ Nulla consequat massa s enim donec pede justo,</li>
      <li><span class="dot"></span>@ Nulla consequat massa s enim donec pede justo,</li>
    </ul>
  </div>
</footer>
<div class="abs fbottom"></div>
<p class="abs copy" style="color:#fff">Copyright 2016 | All Right Reserved</p>
<p class="abs legal" style="color:#fff">Terms &amp; Conditions &nbsp;| Privacy Policy</p>
<a class="abs totop"><svg width="12" height="8" viewBox="0 0 12 8"><path d="M1 7l5-5 5 5" stroke="#fff" stroke-width="2" fill="none"/></svg></a>

</body>
</html>
```